Neudesign Homepage für Computerfirma
Zielgruppe
Wir sind ein seit 12 Jahren lokal ansässiger EDV Dienstleister mit Verkauf von PC, Notebooks etc. mit eigener Reparaturwerkstätte, Handel mit Computerzubehör. Zielgruppe: Klein- bis mittelständige Unternehmen / Organisationen, sowie Privatpersonen aller Altersgruppen.
Aufgabenstellung
Neudesign unserer Homepage: www.brivolt.at
responsives Design unter Beibehaltung unserer Logos bzw. Schriften und Farben( Logo kann gerne dezent verändert werden, aber die Charakteristik und Wiedererkennung muss bleiben ), gerne auch mit Webprogrammierung (CMS) welche aber separat ausgeschrieben/verhandelt wird. Seite soll komplett in HTML werden, technisch am Stand der Zeit mit allen Features die eine moderne HP haben soll.
Slogan "...damit Ihr Computer macht was er soll " wurde bisher schon oft verwendet und sollte wenn möglich eventuell untergebracht werden, gerne animiert.
Im Anhang einige bisher verwendete Grafiken zur Orientierung was bisher schon in Verwendung ist / war. (Bei Bedarf kann mehr geliefert werden)
Das Design sollte Kompetenz, Seriosität, renommiertes Unternehmen vermitteln. Kein Onlineshop momentan geplant. Schwerpunkt Reparatur/Wartung/Dienstleistung mit Ziel der Neukundengewinnung und Info für bestehende Kunden.
Grunddesign der Startseite, bei Bedarf je nach Designvorschlag auch Unterseite / Kontaktformular gerne im Direktauftrag, bei gefallen.

```html
<!DOCTYPE html>
<html lang="de">
<head>
<meta charset="utf-8">
<title>Brivolt – Computersysteme · IT-Solutions</title>
<link rel="stylesheet" href="https://fonts.googleapis.com/css2?family=Arimo:wght@400;700&family=Tinos:ital@1&display=swap">
<style>
  :root{
    --green:#6cb233;
    --green-dark:#5a9e2a;
    --green-light:#a6d92c;
    --ink:#1d1d1d;
    --text:#222;
    --muted:#777;
    --rule:#d8d8d8;
    --footer-bg:#ebebeb;
    --photo:#cfe0f0;
  }
  *{box-sizing:border-box;margin:0;padding:0}
  html,body{width:1186px;height:1200px;overflow:hidden;background:#fff}
  body{position:relative;font-family:"Arimo",Arial,sans-serif;color:var(--text)}
  a{color:inherit;text-decoration:none}
  .abs{position:absolute}

  .top-bar{left:0;top:0;width:1186px;height:4px;background:var(--green)}
  .header-lines{left:0;top:0}

  .brand{left:252px;top:38px;display:flex;align-items:center;gap:8px}
  .brand-dot{width:14px;height:14px;background:var(--ink);border-radius:50%}
  .brand-name{font-size:32px;font-weight:700;color:var(--ink);letter-spacing:1px}
  .brand-sub{left:279px;top:73px;font-size:10px;color:var(--ink)}

  .hotline{left:760px;top:18px;display:flex;align-items:center;gap:10px}
  .hotline-icon{width:31px;height:31px;border-radius:50%;background:var(--green);display:flex;align-items:center;justify-content:center}
  .hotline-label{font-size:10.5px;color:var(--green);letter-spacing:.2px}
  .hotline-number{font-size:16px;color:var(--ink);margin-top:1px}

  .main-nav{left:542px;top:72px;height:43px;display:flex}
  .main-nav a{height:43px;display:flex;align-items:center;padding:0 16px;font-size:12px;color:var(--ink);border-right:1px solid #e4e4e4}
  .main-nav a.home{width:45px;justify-content:center;padding:0;border-left:1px solid #e4e4e4;border-bottom:2px solid var(--green)}

  .hero-photo{left:610px;top:130px;width:280px;height:310px;background:linear-gradient(180deg,#f4f7fb 0%,var(--photo) 60%,#b8c4cf 100%);border-radius:140px 140px 0 0}
  .hero-title{left:252px;top:254px;font-size:28px;color:var(--ink);letter-spacing:.3px}
  .pre{color:var(--green);font-weight:700}
  .hero-slogan{left:252px;top:285px;font-family:"Tinos",serif;font-style:italic;font-size:21px;color:var(--ink)}
  .btn{display:inline-block;background:var(--green);color:#fff;font-size:10.5px;height:22px;line-height:22px;padding:0 15px;box-shadow:2px 2px 0 #c9dfb6;border:1px solid #fff;outline:1px solid var(--green)}
  .hero-btn{left:253px;top:323px}

  .slider-tab{left:541px;top:421px}

  .feature-band{left:0;top:440px;width:1186px;height:211px;background:linear-gradient(100deg,#4ea82f 0%,#66b82e 35%,#8fd02a 65%,#c4e84a 100%)}
  .card{position:absolute;top:462px;width:230px;height:167px;background:#fff;padding:13px 15px}
  .card h2{font-size:20px;font-weight:400;color:var(--ink);padding-bottom:4px;border-bottom:1px solid var(--rule);margin-bottom:16px}
  .card p{font-size:10.3px;line-height:12.5px}
  .card .btn{position:absolute;left:15px;top:130px}

  .panel{position:absolute;top:685px;height:289px;background:#fff;box-shadow:1px 2px 3px rgba(0,0,0,.18)}
  .about{left:237px;width:471px;padding:12px 15px}
  .about h2{font-size:20px;font-weight:700;color:var(--green);letter-spacing:1px;width:200px;padding-bottom:4px;border-bottom:1px solid var(--rule);margin-bottom:16px}
  .about p{font-size:10.3px;line-height:12.5px;width:430px;margin-bottom:12px}
  .about .btn{margin-top:7px}

  .contact{left:719px;width:229px;padding:12px 13px}
  .contact h2{font-size:20px;font-weight:400;color:var(--ink);margin-bottom:6px}
  .shop-photo{width:200px;height:88px;border:2px solid var(--green);background:linear-gradient(120deg,#3a4a3c 0%,#6c8570 45%,#a9c2a0 70%,#4d5a4f 100%);margin-bottom:14px}
  .contact p{font-size:10.3px;line-height:12.5px;margin-bottom:12px}
  .contact .row{display:flex}
  .contact .row span:first-child{width:53px}
  .contact .mail{color:var(--green);text-decoration:underline}

  .site-footer{left:0;top:1009px;width:1186px;height:139px;background:var(--footer-bg);border-top:1px solid #ccc}
  .foot-col{position:absolute;top:1027px;height:121px}
  .foot-col h3{font-size:10px;font-weight:700;color:#777;letter-spacing:.4px;margin-bottom:15px}
  .foot-col a{display:block;font-size:10.3px;line-height:12.6px;color:#8a8a8a}
  .foot-sep{position:absolute;top:1010px;width:1px;height:138px;background:#d4d4d4}

  .bottom-bar{left:0;top:1148px;width:1186px;height:52px;background:var(--green)}
  .bottom-brand{left:245px;top:1155px;font-size:17px;font-weight:700;color:#fff;letter-spacing:1px}
  .bottom-sub{left:250px;top:1176px;font-size:6px;color:#fff}
  .copyright{left:367px;top:1168px;font-size:9px;color:#fff}
  .legal-links{right:237px;top:1168px;font-size:9px;color:#fff}
</style>
</head>
<body>
  <div class="abs top-bar"></div>
  <svg class="abs header-lines" width="1186" height="100" aria-hidden="true">
    <line x1="0" y1="95" x2="240" y2="95" stroke="#6cb233" stroke-width="1.5"/>
    <line x1="440" y1="70" x2="1186" y2="70" stroke="#6cb233" stroke-width="1.5"/>
  </svg>

  <a class="abs brand" href="#"><span class="brand-dot"></span><span class="brand-name">BRIVOLT</span></a>
  <div class="abs brand-sub">Computersysteme · IT-Solutions</div>

  <div class="abs hotline">
    <div class="hotline-icon">
      <svg width="16" height="16" viewBox="0 0 24 24" aria-hidden="true"><path fill="#fff" d="M6.6 10.8a15.1 15.1 0 0 0 6.6 6.6l2.2-2.2c.3-.3.7-.4 1-.2 1.1.4 2.3.6 3.6.6.6 0 1 .4 1 1V20c0 .6-.4 1-1 1A17 17 0 0 1 3 4c0-.6.4-1 1-1h3.5c.6 0 1 .4 1 1 0 1.3.2 2.5.6 3.6.1.3 0 .7-.2 1z"/></svg>
    </div>
    <div>
      <div class="hotline-label">PERSÖNLICHE BERATUNG</div>
      <div class="hotline-number">+43 55 76 41 28 0</div>
    </div>
  </div>

  <nav class="abs main-nav">
    <a class="home" href="#" aria-label="Startseite">
      <svg width="12" height="11" viewBox="0 0 12 11" aria-hidden="true"><path fill="#6cb233" d="M6 0 0 5.5h1.6V11h3.3V7.5h2.2V11h3.3V5.5H12z"/></svg>
    </a>
    <a href="#">SERVICE</a>
    <a href="#">AKTUELLES</a>
    <a href="#">BRIVOLT</a>
    <a href="#">KONTAKT</a>
  </nav>

  <div class="abs hero-photo" role="img" aria-label="Foto: lächelnder Techniker im hellblauen Hemd mit Laptop unter dem Arm"></div>
  <h1 class="abs hero-title"><span class="pre">BRI</span>REPARATUR</h1>
  <div class="abs hero-slogan">...damit Ihr Computer macht was er soll</div>
  <a class="abs btn hero-btn" href="#">Mehr erfahren</a>

  <div class="abs feature-band" role="img" aria-label="Grüner Hintergrund mit Dreiecksmuster"></div>
  <svg class="abs slider-tab" width="104" height="19" aria-hidden="true">
    <polygon points="10,0 94,0 104,19 0,19" fill="#6cb233"/>
    <circle cx="22" cy="10" r="5" fill="#fff"/><circle cx="37" cy="10" r="5" fill="#fff"/>
    <circle cx="52" cy="10" r="5" fill="#a6d92c"/><circle cx="67" cy="10" r="5" fill="#fff"/>
    <circle cx="82" cy="10" r="5" fill="#fff"/>
  </svg>

  <section class="card" style="left:237px">
    <h2><span class="pre">BRI</span>MOBIL</h2>
    <p>Ob Sie die Lieferung und Inbetriebnahme eines neuen PC´s oder einfach eine Beratung oder Reparatur wünschen wir kommen gerne zu Ihnen ins Haus.</p>
    <a class="btn" href="#">Mehr erfahren</a>
  </section>
  <section class="card" style="left:477px">
    <h2><span class="pre">BRI</span>BERATUNG</h2>
    <p>Unsere Techniker haben das Ziel, jedem Kunden durch kompetente Beratung, Planung und Umsetzung ein individuell konfiguriertes, skalierbares und betriebssicheres System zu installieren.</p>
    <a class="btn" href="#">Mehr erfahren</a>
  </section>
  <section class="card" style="left:718px">
    <h2><span class="pre">BRI</span>REPARATUR</h2>
    <p>Wir überprüfen, reparieren und erweitern Computer und Peripheriegeräte von sämtlichen Herstellern.</p>
    <a class="btn" href="#">Mehr erfahren</a>
  </section>

  <section class="panel about">
    <h2>BRIVOLT</h2>
    <p>Ein Ziel unserer Geschäftspolitik ist es, durch Zuverlässigkeit, Schnelligkeit und Kompetenz mit unseren Kunden ein partnerschaftliches Verhältnis zu erreichen.</p>
    <p>Wenn Sie die Zusammenarbeit mit uns gewählt haben, werden Sie schnell feststellen, dass wir als Ihr Geschäftspartner unser Hauptaugenmerk nicht allein auf den Vertrieb lenken, sondern als Maxime allen Handelns die Zufriedenheit unserer Kunden in den Vordergrund stellen.</p>
    <p>Nicht nur durch jahrelange praktische Erfahrung wissen wir, dass eine faire, kompetente Beratung und entsprechend praxisorientierte Problemlösung der Weg zu Ihrem Erfolg ist.</p>
    <p>Ein gewachsener Stamm überzeugter Kunden bestätigt die Anerkennung im Markt und ist ein Beweis für die Richtigkeit unserer Geschäftspolitik.</p>
    <a class="btn" href="#">Mehr erfahren</a>
  </section>

  <section class="panel contact">
    <h2><span class="pre">BRI</span>KONTAKT</h2>
    <div class="shop-photo" role="img" aria-label="Foto: Schaufenster des Geschäfts mit Firmenschriftzug"></div>
    <p><b>Brivolt - Computersysteme</b><br>Lindenhofweg 14<br>A-6830 Rankwil</p>
    <p><span class="row"><span>Telefon:</span><span>05576 / 41280</span></span><span class="row"><span>Fax:</span><span>05576 / 41280 - 21</span></span></p>
    <p class="row"><span>E-Mail:</span><a class="mail" href="#">office@brivolt.at</a></p>
    <p><b>Öffnungszeiten</b><br>Montag - Freitag: &nbsp;&nbsp;&nbsp;&nbsp;13.30 Uhr - 19.00 Uhr</p>
  </section>

  <footer>
    <div class="abs site-footer"></div>
    <div class="foot-sep" style="left:415px"></div>
    <div class="foot-sep" style="left:593px"></div>
    <div class="foot-sep" style="left:771px"></div>
    <div class="foot-col" style="left:252px"><h3>SERVICE</h3><a href="#">BRIMobil</a><a href="#">BRIBeratung</a><a href="#">BRIPremium</a><a href="#">BRIReparatur</a><a href="#">BRIRecycling</a></div>
    <div class="foot-col" style="left:431px"><h3>BRIVOLT</h3><a href="#">Porttrait</a><a href="#">Portfolio</a><a href="#">Handel</a><a href="#">Dienstleitungen</a><a href="#">Referenzen</a><a href="#">Empfehlen Sie uns</a></div>
    <div class="foot-col" style="left:609px"><h3>AKTUELLES</h3><a href="#">BRIflash</a><a href="#">Projekte</a><a href="#">Sponsoring</a></div>
    <div class="foot-col" style="left:787px"><h3>KONTAKT</h3><a href="#">Kontaktformular</a><a href="#">PCNotdienst</a><a href="#">Kontaktadressen</a><a href="#">Öffnungszeiten</a><a href="#">Lageplan</a></div>

    <div class="abs bottom-bar"></div>
    <div class="abs bottom-brand">BRIVOLT</div>
    <div class="abs bottom-sub">Computersysteme · IT-Solutions</div>
    <div class="abs copyright">© BRIVOLT - Computersysteme-IT-Solutions</div>
    <div class="abs legal-links"><a href="#">Sitemap</a> &nbsp;| &nbsp;<a href="#">Kontakt</a> &nbsp;| &nbsp;<a href="#">Impressum</a></div>
  </footer>
</body>
</html>
```